Local Contractor needs Upscale Web Design

This website needs to have an upscale look with a very modern feel.

This is for a home page psd layout

Please build your psd file to match the look of this template: http://www.layoutquarry.example/demo/38162.html

Please change the color scheme to the colors of the attached logo

Add Logo that is attached.

Phone Number:
507-392-4186

Must Include these pages in a horizontal menu bar in this order:
Home, About, Services, Portfolio, Testimonials, Contact

For the rotating banners:
1. Construction - 35+ Years and Growing
2. Capabilities - Complete Line of Services
3. Commitment - Quality and Attention to Detail

Images under rotating banner:
Image 1, 2, 3 (Attached - Crop to fit)

What We're Thinking Section - Change title text to "Retail Space Construction" (Fill the remainder with latin text)

Who Are We Section - Change title text to "Industrial Construction" (Fill the remainder with latin text)

Project Gallery - Image 4, 5, 6, 7 (Attached - Crop to fit)

Remove the sections towards the bottom titled "Why Us" & "Services"

Please make the map show this address:
2917 86th St SW, Pine Hollow, MN 55104

Footer:
Ridgeway Bolt Construction © 2015 | Powered by Marlo Pixel Works

```html
<!DOCTYPE html>
<html lang="en">
<head>
<meta charset="utf-8">
<title>Ridgeway Bolt Construction — Home</title>
<link href="https://fonts.googleapis.com/css2?family=Bebas+Neue&family=Montserrat:wght@700&family=Open+Sans:wght@600&display=swap" rel="stylesheet">
<style>
  :root {
    --stage: #888888;
    --brand-red: #972a30;
    --brand-red-deep: #862328;
    --white: #ffffff;
    --rule: rgba(255,255,255,0.25);
    --dot-dim: rgba(255,255,255,0.6);
    --photo-brick: #8a6a5a;
    --photo-sky: #c9ccd0;
    --photo-stone: #b59a78;
  }
  * { margin: 0; padding: 0; box-sizing: border-box; }
  html, body { width: 1200px; height: 1000px; overflow: hidden; }
  body { background: var(--stage); position: relative; font-family: "Open Sans", sans-serif; }

  .site {
    position: absolute; left: 50px; top: 242px;
    width: 1100px; height: 666px; overflow: hidden;
    background: var(--white);
  }
  .hero {
    position: absolute; left: 0; top: 0; width: 1100px; height: 478px;
    background: radial-gradient(ellipse at 60% 30%, var(--brand-red) 0%, var(--brand-red-deep) 100%);
    color: var(--white);
  }
  .topbar {
    position: absolute; left: 0; top: 0; width: 100%; height: 36px;
    border-bottom: 1px solid var(--rule);
  }
  .topbar-phone {
    position: absolute; right: 69px; top: 9px;
    font-size: 13px; font-weight: 600; letter-spacing: 0.3px;
    display: flex; align-items: center; gap: 6px;
  }
  .brand {
    position: absolute; left: 70px; top: 66px;
    display: flex; align-items: center; gap: 10px;
  }
  .brand-mark { width: 22px; height: 22px; background: var(--white); }
  .brand-name {
    font-family: "Bebas Neue", sans-serif; font-size: 30px; line-height: 1;
    letter-spacing: 1px; color: var(--white);
  }
  .main-nav {
    position: absolute; right: 69px; top: 60px;
    display: flex; gap: 24px; list-style: none;
  }
  .main-nav li {
    font-family: "Bebas Neue", sans-serif; font-size: 23px; letter-spacing: 0.8px;
    position: relative;
  }
  .main-nav li.is-active::after {
    content: ""; position: absolute; left: -6px; right: -6px; top: 50px;
    height: 2px; background: var(--white);
  }
  .hero-title {
    position: absolute; left: 68px; top: 178px;
    font-family: "Bebas Neue", sans-serif; font-size: 126px; line-height: 1;
    letter-spacing: 3px;
  }
  .hero-tagline {
    position: absolute; left: 70px; top: 295px;
    font-family: "Montserrat", sans-serif; font-weight: 700; font-size: 25px;
    letter-spacing: 0.5px;
  }
  .slider-dots {
    position: absolute; left: 522px; top: 445px; display: flex; gap: 16px;
  }
  .slider-dots span { width: 8px; height: 8px; border-radius: 50%; background: var(--dot-dim); }
  .slider-dots span.is-current { background: var(--white); }

  .feature-photo { position: absolute; top: 510px; height: 160px; }
  .feature-photo--wide {
    left: 71px; width: 631px;
    background: linear-gradient(180deg, var(--photo-sky) 0%, var(--photo-sky) 28%, var(--photo-brick) 28%, #7a5446 100%);
  }
  .feature-photo--narrow {
    left: 732px; width: 299px;
    background: linear-gradient(180deg, var(--photo-sky) 0%, var(--photo-stone) 30%, #9c8260 100%);
  }
</style>
</head>
<body>
  <main class="site">
    <header class="hero">
      <div class="topbar">
        <div class="topbar-phone">
          <svg width="13" height="13" viewBox="0 0 24 24" aria-hidden="true"><path fill="#fff" d="M6.6 10.8a15.1 15.1 0 0 0 6.6 6.6l2.2-2.2c.3-.3.7-.4 1-.2 1.1.4 2.3.6 3.6.6.6 0 1 .4 1 1V20c0 .6-.4 1-1 1A17 17 0 0 1 3 4c0-.6.4-1 1-1h3.5c.6 0 1 .4 1 1 0 1.3.2 2.5.6 3.6.1.3 0 .7-.2 1z"/></svg>
          507-392-4186
        </div>
      </div>
      <div class="brand">
        <span class="brand-mark"></span>
        <span class="brand-name">Ridgeway Bolt Construction</span>
      </div>
      <ul class="main-nav">
        <li class="is-active">Home</li>
        <li>About</li>
        <li>Services</li>
        <li>Portfolio</li>
        <li>Testimonials</li>
        <li>Contact</li>
      </ul>
      <h1 class="hero-title">CONSTRUCTION</h1>
      <p class="hero-tagline">35+ YEARS AND GROWING</p>
      <div class="slider-dots"><span class="is-current"></span><span></span><span></span></div>
    </header>
    <div class="feature-photo feature-photo--wide" role="img" aria-label="Photo of a brick retail building with a saloon sign"></div>
    <div class="feature-photo feature-photo--narrow" role="img" aria-label="Photo of a beige retail storefront at a corner"></div>
  </main>
</body>
</html>
```